Business Card Design

I need a business card design for my new solo law practice. I practice consumer bankruptcy law.

I would like a simple, functional business card that looks professional but will also be understandable to regular people - not just other lawyers.
Updates

I added a couple of possible logos that can be incorporated

I'm sorry about the confusion, but the suite number for my new office is suite #150. Thanks for your patience

Target Market(s)

the real target market is potential clients

Industry/Entity Type

Business

Contact Information for Business Card

Law Offices of Dorian P. Whitcombe
Dorian P. Whitcombe
Attorney at Law
Bankruptcy Law
487 Mariner Court #260
Fernley Bay, PA 19042
(555) 318-7264 (Phone)
(555) 318-7290 (Fax)
dorianw@fernleydebtrelief.example
fernleydebtrelief.example

Font styles to use
Serif

Requirements
Nice to have
• I've added some possible logos to possible incorporate

```html
<!DOCTYPE html>
<html lang="en">
<head>
<meta charset="utf-8">
<title>Dorian P. Whitcombe – Business Card</title>
<link rel="stylesheet" href="https://fonts.googleapis.com/css2?family=Arimo:wght@400;700&display=swap">
<style>
  :root {
    --backdrop: #e9e9ec;
    --card: #ffffff;
    --band-red: #b0141b;
    --band-blue: #284a74;
    --icon-red: #c8232b;
    --ink: #1c1c1c;
    --ink-soft: #333333;
  }
  * { box-sizing: border-box; margin: 0; padding: 0; }
  html, body {
    width: 1200px; height: 900px; overflow: hidden;
    background: var(--backdrop);
    font-family: "Arimo", Arial, sans-serif;
    color: var(--ink);
  }
  .business-card {
    position: absolute; left: 75px; top: 150px;
    width: 1050px; height: 600px;
    background: var(--card);
    box-shadow: 0 10px 30px rgba(0,0,0,.18);
    overflow: hidden;
  }
  .band { position: absolute; top: 0; bottom: 0; width: 48px; }
  .band--red { left: 0; background: var(--band-red); }
  .band--blue { right: 0; background: var(--band-blue); }

  .firm-mark {
    position: absolute; left: 110px; top: 250px;
    display: flex; align-items: center; gap: 18px;
    width: 420px;
  }
  .firm-mark__dot {
    flex: none; width: 26px; height: 26px; border-radius: 50%;
    background: var(--band-red);
  }
  .firm-mark__name {
    font-size: 26px; font-weight: 700; line-height: 1.25;
    text-transform: uppercase; color: var(--ink);
  }

  .identity {
    position: absolute; right: 110px; top: 70px;
    text-align: right;
  }
  .identity__name {
    font-size: 40px; font-weight: 700; text-transform: uppercase;
    letter-spacing: .5px; margin-bottom: 10px;
  }
  .identity__role { font-size: 28px; line-height: 1.25; color: var(--ink-soft); }

  .address {
    position: absolute; left: 110px; bottom: 60px;
    display: flex; gap: 12px; font-size: 27px; line-height: 1.3;
    font-style: normal; color: var(--ink-soft);
  }
  .address svg { margin-top: 4px; }

  .contact {
    position: absolute; right: 90px; bottom: 60px;
    list-style: none; text-align: right; font-size: 27px; line-height: 1.3;
    color: var(--ink-soft);
  }
  .contact li { display: flex; justify-content: flex-end; align-items: center; gap: 12px; }
  .icon { width: 22px; height: 22px; flex: none; }
</style>
</head>
<body>
  <main class="business-card">
    <div class="band band--red"></div>
    <div class="band band--blue"></div>

    <header class="identity">
      <h1 class="identity__name">Dorian P. Whitcombe</h1>
      <p class="identity__role">Attorney at Law</p>
      <p class="identity__role">Bankruptcy Law</p>
    </header>

    <div class="firm-mark">
      <span class="firm-mark__dot"></span>
      <span class="firm-mark__name">Law Offices of<br>Dorian P. Whitcombe</span>
    </div>

    <address class="address">
      <svg class="icon" viewBox="0 0 24 24" aria-hidden="true">
        <path d="M12 2a7 7 0 0 0-7 7c0 5 7 13 7 13s7-8 7-13a7 7 0 0 0-7-7z" fill="var(--icon-red)"/>
        <circle cx="12" cy="9" r="2.6" fill="#fff"/>
      </svg>
      <span>487 Mariner Court<br>#260<br>Fernley Bay, PA 19042</span>
    </address>

    <ul class="contact">
      <li>(555) 318-7264
        <svg class="icon" viewBox="0 0 24 24" aria-hidden="true">
          <path d="M6.5 3l3 4-2 2.2c1.2 2.6 3.3 4.7 5.8 5.8l2.2-2 4 3-1.6 3.6C11 19.8 4.2 13 3 4.6z" fill="var(--icon-red)"/>
        </svg>
      </li>
      <li>(555) 318-7290
        <svg class="icon" viewBox="0 0 24 24" aria-hidden="true">
          <rect x="6" y="3" width="12" height="6" fill="var(--icon-red)"/>
          <rect x="3" y="9" width="18" height="9" rx="2" fill="var(--icon-red)"/>
          <rect x="7" y="14" width="10" height="7" fill="#fff" stroke="var(--icon-red)" stroke-width="1.5"/>
        </svg>
      </li>
      <li>dorianw@fernleydebtrelief.example
        <svg class="icon" viewBox="0 0 24 24" aria-hidden="true">
          <rect x="3" y="5" width="18" height="14" rx="1.5" fill="var(--icon-red)"/>
          <path d="M3.5 6l8.5 7 8.5-7" fill="none" stroke="#fff" stroke-width="1.6"/>
        </svg>
      </li>
      <li>fernleydebtrelief.example
        <svg class="icon" viewBox="0 0 24 24" aria-hidden="true">
          <circle cx="10" cy="10" r="6" fill="none" stroke="var(--icon-red)" stroke-width="2.4"/>
          <path d="M14.5 14.5l6 6" stroke="var(--icon-red)" stroke-width="2.6" stroke-linecap="round"/>
        </svg>
      </li>
    </ul>
  </main>
</body>
</html>
```